Bold Modern Creative Wine Label Needed for a Chardonnay

We need a modern, eye catching label, one that will appeal to millennials, but also attract the older more conservative crowd. We like the boldness of black on white but are open to your suggestions. Since the bottle type is a light green 'burgundy style' bottle, you should take that into account. The name of the brand is Ko`. The attached label is example of what we like very much. It is eye catching and bold and modern. Keep in mind that the bottle will be light green in color so black and white might not work so well. Use your creativity please! The label can be any size but needs to fit on this shape bottle. See attached photos. thanks!!

(Please no grapes or wine glasses or wine bottles featured on the label!)

Hi Designers, I just wanted to let you know that we received many great designs and we are sorting through them this week. The website is making it a bit difficult to create a 'poll' so this is taking longer than we expected. Thanks for all the great submissions!

```html
<!DOCTYPE html>
<html lang="en">
<head>
<meta charset="utf-8">
<title>Ko` Chardonnay Label</title>
<link rel="stylesheet" href="https://fonts.googleapis.com/css2?family=Cinzel:wght@400;700&family=Tinos&display=swap">
<style>
  :root {
    --canvas: #ffffff;
    --label-light: #f6f7f9;
    --label-mid: #eceef0;
    --label-shade: #d6d6d6;
    --ink-dark: #2a2d10;
    --ink-olive: #6d7a1c;
    --ink-body: #1e1e1e;
  }
  * { margin: 0; padding: 0; box-sizing: border-box; }
  html, body {
    width: 1200px;
    height: 1200px;
    overflow: hidden;
    background: var(--canvas);
  }
  .canvas {
    position: relative;
    width: 1200px;
    height: 1200px;
  }
  .label {
    position: absolute;
    left: 200px;
    top: 238px;
    width: 800px;
    height: 724px;
    background: linear-gradient(90deg, var(--label-light) 0%, var(--label-mid) 45%, var(--label-shade) 100%);
  }
  .brand-name {
    position: absolute;
    left: 130px;
    top: 110px;
    width: 500px;
    text-align: center;
    font-family: "Cinzel", serif;
    font-weight: 700;
    font-size: 260px;
    line-height: 1;
    letter-spacing: -4px;
    color: var(--ink-dark);
  }
  .vintage {
    position: absolute;
    left: 42px;
    top: 390px;
    font-family: "Cinzel", serif;
    font-weight: 400;
    font-size: 44px;
    line-height: 1;
    color: var(--ink-olive);
  }
  .wine-type {
    position: absolute;
    left: 0;
    top: 520px;
    width: 800px;
    padding-left: 20px;
    text-align: center;
    font-family: "Cinzel", serif;
    font-weight: 400;
    font-size: 50px;
    line-height: 1;
    color: var(--ink-olive);
  }
  .tagline {
    position: absolute;
    left: 0;
    top: 612px;
    width: 800px;
    padding-left: 20px;
    text-align: center;
    font-family: "Tinos", serif;
    font-size: 20px;
    line-height: 34px;
    color: var(--ink-body);
  }
</style>
</head>
<body>
  <main class="canvas">
    <section class="label">
      <h1 class="brand-name">Ko`</h1>
      <p class="vintage">2019</p>
      <p class="wine-type">White Wine</p>
      <p class="tagline">Lorem ipsum dolor sit amet,<br>consectetuer adipiscing elit,</p>
    </section>
  </main>
</body>
</html>
```